Buch-/eBook-Cover Budgetplanung
Zielgruppe
Ich bin Autorin und verkaufe unter meiner Marke SparLaterne Bücher und handgemachte Produkte rund um Budgetplanung und bewussten Umgang mit Geld. Meine Zielgruppe sind Frauen ab 45, die ihre Finanzen ordnen und bewusster leben möchten. Sie mögen eine ruhige, hochwertige, leicht nostalgische Ästhetik und werden von lauten, grellen Designs abgeschreckt.
Aufgabenstellung
Buchcover 'Der leere Korb' (VRL), Auftakt einer Cover-Serie
Das Buch:
Ratgeber über bewussten Konsumverzicht: ein Jahr Kaufpause mit monatlichen Challenges. Warm und ermutigend, kein Verbotsbuch. Zielgruppe: Frauen ab 45, die eine ruhige, hochwertige, leicht nostalgische Ästhetik mögen.
Texte auf dem Cover:
Titel: Der leere Korb
Untertitel: Die No-Buy-Challenge: Ein Jahr bewusst nicht kaufen, Geld sparen und herausfinden, was du wirklich brauchst
Autorin: Helene Morwitz
Serie:
Weitere Geld-Ratgeber von mir erhalten danach Cover im selben Stil. Gesucht ist also ein wiederholbares Layout, bei dem sich pro Buch nur Titel und Motiv ändern. Der Gewinner erhält die Folgecover als Direktaufträge.
Stil (Referenzbilder anbei, bitte verbindlich umsetzen):
Marke SparLaterne: Graublau (#95a9af) und Creme, Gold nur als Akzent. Vertikale Streifen als Markenmuster, weiße Spitzenborte, schwarze handgezeichnete Schleife (PNG liegt bei). Schriften: Cormorant Garamond für Versalien, Sloop Pro, Kalligrafieschrift für Akzente. Wirkung: elegantes, feminines Vintage. Das Buchinnere ist bereits in diesem Stil gestaltet (Beispielseiten anbei), das Cover soll dazu passen.
Bitte nicht: Geldscheine, Münzen, Sparschweine, Einkaufstüten, rote Verbotssymbole, grelle Farben, Rosa, überfüllte Layouts.
Wichtigstes Kriterium:
Der Titel muss als kleines Lunova-Vorschaubild klar lesbar sein.
Lieferumfang:
E-Book-Cover (JPG, 2560 x 1600 px), VRL-Print-Umschlag (6 x 9 Zoll, 159 Seiten, Farbdruck)
Das Design darf nicht zu überladen sein.

```html
<!DOCTYPE html>
<html lang="de">
<head>
<meta charset="utf-8">
<title>Der leere Korb – Umschlag</title>
<link rel="stylesheet" href="https://fonts.googleapis.com/css2?family=Cormorant+Garamond:ital,wght@0,500;0,600;0,700;1,500&family=EB+Garamond:ital,wght@0,400;1,400&family=Pinyon+Script&display=swap">
<style>
  :root{
    --slate:#94a9af;
    --cream:#f6f2ea;
    --paper:#fdfaf4;
    --copper:#b57c4c;
    --gold:#d8b67a;
    --ink:#211f1d;
    --lace:#c9d4d6;
    --guide-blue:#2a3cff;
  }
  *{margin:0;padding:0;box-sizing:border-box}
  html,body{width:1200px;height:886px;overflow:hidden;background:var(--slate)}
  .stage{position:relative;width:1200px;height:886px;background:var(--slate);overflow:hidden}

  .wrap{position:absolute;left:50px;top:50px;width:1102px;height:785px;
    border:1px solid #222;
    background:repeating-linear-gradient(90deg,var(--slate) 0 22px,var(--cream) 22px 43px);}
  .spine{position:absolute;left:493px;top:0;width:115px;height:100%;background:var(--slate)}
  .spine-text{position:absolute;left:590px;top:148px;width:24px;height:600px;
    writing-mode:vertical-rl;line-height:24px;white-space:nowrap;
    font-family:"Cormorant Garamond",serif;font-weight:500;font-size:20px;color:var(--cream);letter-spacing:.3px}
  .spine-text .star{color:var(--gold);padding:10px 0;font-weight:400}

  .lace{position:absolute;top:0;height:100%;background:var(--lace)}
  .lace.back{left:0;width:38px}
  .lace.front{right:0;width:46px}

  .guide{position:absolute;top:0;height:886px;width:0}
  .guide.trim{border-left:1px dotted var(--guide-blue)}
  .guide.fold{border-left:1px dashed #333}

  /* back panel */
  .back-card{position:absolute;left:113px;top:139px;width:428px;height:558px}
  .back-card svg{position:absolute;inset:0}
  .back-content{position:absolute;left:34px;top:36px;width:360px;color:var(--ink)}
  .hook{font-family:"Pinyon Script",cursive;font-weight:400;font-size:33px;line-height:38px;text-align:center;margin-bottom:16px}
  .divider{display:flex;align-items:center;gap:10px;margin:0 0 14px}
  .divider::before,.divider::after{content:"";flex:1;height:1px;background:var(--gold)}
  .divider i{color:var(--gold);font-style:normal;font-size:14px}
  .divider.dot i{font-size:8px}
  .blurb p{font-family:"EB Garamond",serif;font-size:12.6px;line-height:18px;text-align:justify;margin-bottom:8px}
  .bio{font-family:"EB Garamond",serif;font-style:italic;font-size:12.6px;line-height:18px;text-align:justify}

  /* front panel */
  .front-card{position:absolute;left:670px;top:153px;width:438px;height:518px}
  .front-card svg.frame{position:absolute;inset:0}
  .bow{position:absolute;left:194px;top:34px;width:50px;height:28px;background:#2b2a28;border-radius:40% 40% 30% 30%}
  .title{position:absolute;left:0;right:0;top:80px;text-align:center;font-family:"Cormorant Garamond",serif;
    font-weight:700;font-size:58px;line-height:62px;color:var(--ink)}
  .subtitle{position:absolute;left:0;right:0;top:205px;text-align:center;font-family:"Cormorant Garamond",serif;
    font-weight:600;font-size:30px;line-height:36px;color:var(--gold)}
  .motif{position:absolute;left:121px;top:250px;width:196px;height:150px;
    background:radial-gradient(ellipse at center,#8c8c8a 0%,#c9c6c0 60%,var(--paper) 100%);border-radius:8px}
  .tagline{position:absolute;left:0;right:0;top:414px;text-align:center;font-family:"EB Garamond",serif;
    font-size:18.5px;line-height:21px;color:var(--ink)}
  .author{position:absolute;left:670px;width:438px;top:715px;text-align:center;font-family:"Cormorant Garamond",serif;
    font-weight:600;font-size:33px;line-height:40px;color:var(--ink)}
</style>
</head>
<body>
<div class="stage">
  <div class="wrap">
    <div class="lace back" role="img" aria-label="Weiße Spitzenborte"></div>
    <div class="lace front" role="img" aria-label="Weiße Spitzenborte"></div>
    <div class="spine"></div>
  </div>

  <div class="guide trim" style="left:543px"></div>
  <div class="guide trim" style="left:578px"></div>
  <div class="guide fold" style="left:624px"></div>
  <div class="guide fold" style="left:658px"></div>

  <p class="spine-text">Der leere Korb<span class="star">✱</span>Die No-Buy- Challenge<span class="star">✱</span>Helene Morwitz</p>

  <!-- back cover -->
  <div class="back-card">
    <svg viewBox="0 0 428 558" width="428" height="558">
      <path d="M26 0H402A26 26 0 0 0 428 26V532A26 26 0 0 0 402 558H26A26 26 0 0 0 0 532V26A26 26 0 0 0 26 0Z" fill="#fdfaf4" stroke="#e6cfae" stroke-width="1.5"/>
      <path d="M36 10H392A26 26 0 0 0 418 36V522A26 26 0 0 0 392 548H36A26 26 0 0 0 10 522V36A26 26 0 0 0 36 10Z" fill="none" stroke="#b57c4c" stroke-width="1.5"/>
      <path d="M42 18H386A26 26 0 0 0 410 42V516A26 26 0 0 0 386 540H42A26 26 0 0 0 18 516V42A26 26 0 0 0 42 18Z" fill="none" stroke="#b57c4c" stroke-width="1" stroke-dasharray="1 3"/>
    </svg>
    <div class="back-content">
      <h2 class="hook">Was wäre, wenn du ein<br>Jahr lang nichts kaufst?</h2>
      <div class="divider"><i>✱</i></div>
      <div class="blurb">
        <p>Kein neues Oberteil. Keine Deko. Kein „Das gönn ich mir jetzt mal“.</p>
        <p>Klingt nach Verzicht? Ist es nicht. Dieses Buch verbietet dir nichts. Es lädt dich ein, ein Jahr lang bewusst zu leben, statt nebenbei zu konsumieren.</p>
        <p>Es begleitet dich durch dein Jahr: mit Checklisten zu jedem Thema und zwölf No-Buy-Challenges zum Ankreuzen. Du findest heraus, was du wirklich brauchst, warum du oft nur aus Gewohnheit oder Frust kaufst und was du mit dem gesparten Geld alles erreichen kannst.</p>
        <p>Am Ende wirst du merken: Dir fehlt nichts. Aber du hast mehr. Mehr Geld, mehr Klarheit, mehr Leben.</p>
      </div>
      <div class="divider dot"><i>●</i></div>
      <p class="bio">Helene Morwitz budgetiert seit den 1990er Jahren mit der Umschlagmethode und hat ihren Weg aus Schulden und Konsumdruck selbst gemeistert. Sie weiß: Verzicht ist kein Verlust. Er ist der Anfang von etwas Besserem.</p>
    </div>
  </div>

  <!-- front cover -->
  <div class="front-card">
    <svg class="frame" viewBox="0 0 438 518" width="438" height="518">
      <path d="M40 18C120 18 170 0 219 0C268 0 318 18 398 18A40 40 0 0 0 438 58V460A40 40 0 0 0 398 500C318 500 268 518 219 518C170 518 120 500 40 500A40 40 0 0 0 0 460V58A40 40 0 0 0 40 18Z" fill="#fdfaf4" stroke="#e6cfae" stroke-width="1.5"/>
      <path d="M46 28C124 28 172 10 219 10C266 10 314 28 392 28A36 36 0 0 0 428 64V454A36 36 0 0 0 392 490C314 490 266 508 219 508C172 508 124 490 46 490A36 36 0 0 0 10 454V64A36 36 0 0 0 46 28Z" fill="none" stroke="#b57c4c" stroke-width="1.6"/>
      <path d="M52 37C128 37 174 19 219 19C264 19 310 37 386 37A32 32 0 0 0 419 70V448A32 32 0 0 0 386 481C310 481 264 499 219 499C174 499 128 481 52 481A32 32 0 0 0 19 448V70A32 32 0 0 0 52 37Z" fill="none" stroke="#b57c4c" stroke-width="1" stroke-dasharray="1 3"/>
    </svg>
    <div class="bow" role="img" aria-label="Schwarze handgezeichnete Schleife"></div>
    <h1 class="title">Der leere<br>Korb</h1>
    <p class="subtitle">Die No-Buy-Challenge</p>
    <div class="motif" role="img" aria-label="Gezeichneter leerer Einkaufswagen mit zarten Zweigen"></div>
    <p class="tagline">Ein Jahr bewusst nicht kaufen,<br>Geld sparen und herausfinden,<br>was du wirklich brauchst</p>
  </div>
  <p class="author">Helene Morwitz</p>
</div>
</body>
</html>
```